Brellmoor Cosmetic Doctor is the title and the name of the business

Facebook advertising: keep
To those dimensions

Aimed at Caucasian women between the ages of 18 - 60 interested in beauty and cosmetic injectables. Will be boosted on facebook which is my advertising platform.

Name: Brellmoor Cosmetic Doctor
0400 555 271

Forehead $58
Frown lines $116
Crows feet $116
Lip fillers $380

I would like to have a beautiful girl that suits the picture.

Target Market(s)

Females between 18 - 60 interested in Lumarex and cosmetic fillers
Prefer Caucasian as that's the majority of population

Industry/Entity Type

Beauty Salon

Font styles to use
Serif
Script

Colors
e667a6
eea4c8
f9d9e8
fee18a
fbf289
fbee3d
cadf82
cedeed
85cae6

Requirements
Must have
• Name: Brellmoor Cosmetic Doctor
• Phone number: 0400 559 271
• Prices:
• Forehead $58
• Frown lines $116
• Crows feet $116
• Lip fillers $380
• Picture of female that is very beautiful
Nice to have
• Not a cartoon or anything else that's not a real picture of a female
Should not have
• No cartoon pictures. Proper picture of women

```html
<!DOCTYPE html>
<html lang="en">
<head>
<meta charset="utf-8">
<title>Brellmoor Cosmetic Doctor</title>
<link rel="stylesheet" href="https://fonts.googleapis.com/css2?family=Great+Vibes&family=Lato:wght@400&display=swap">
<style>
  :root {
    --pink-base: #eca1c8;
    --pink-band: #fbc2e0;
    --pink-glow: #f9d9e8;
    --skin-light: #f2d9cc;
    --skin-mid: #ecc8b8;
    --white: #ffffff;
  }
  * { margin: 0; padding: 0; box-sizing: border-box; }
  html, body {
    width: 1200px;
    height: 628px;
    overflow: hidden;
    background: var(--pink-base);
  }
  .ad {
    position: relative;
    width: 1200px;
    height: 628px;
    overflow: hidden;
    background:
      linear-gradient(115deg, rgba(249,217,232,0) 0%, rgba(249,217,232,0.6) 36%, rgba(249,217,232,0) 55%),
      var(--pink-base);
  }
  .model-photo {
    position: absolute;
    left: 0;
    top: 0;
    width: 520px;
    height: 628px;
    background:
      linear-gradient(90deg, var(--skin-light) 0%, var(--skin-mid) 30%, rgba(240,196,205,0.85) 62%, rgba(236,161,200,0) 100%);
  }
  .treatment-map {
    position: absolute;
    left: 0;
    top: 0;
    width: 500px;
    height: 628px;
  }
  .price-label {
    position: absolute;
    font-family: "Great Vibes", cursive;
    font-size: 27px;
    line-height: 1;
    color: var(--white);
    white-space: nowrap;
  }
  .price-forehead { right: 748px; top: 66px; }
  .price-frown { right: 772px; top: 121px; }
  .price-crows { right: 824px; top: 228px; }
  .price-lips { right: 784px; top: 356px; }

  .title-band {
    position: absolute;
    left: 520px;
    top: 165px;
    width: 680px;
    height: 243px;
    background: linear-gradient(90deg, rgba(251,194,224,0.35) 0%, var(--pink-band) 55%, var(--pink-band) 100%);
  }
  .business-name {
    position: absolute;
    left: 598px;
    top: 186px;
    font-family: "Great Vibes", cursive;
    font-weight: 400;
    font-size: 95px;
    line-height: 92px;
    color: var(--white);
    white-space: nowrap;
  }
  .business-name span { display: block; }
  .business-name .line-two { margin-left: 12px; }

  .call-line {
    position: absolute;
    right: 33px;
    bottom: 22px;
    font-family: "Lato", sans-serif;
    font-size: 26px;
    color: var(--white);
  }
</style>
</head>
<body>
<main class="ad">
  <div class="model-photo" role="img" aria-label="Photo of a beautiful young woman with smooth skin, half face and bare shoulder"></div>

  <svg class="treatment-map" viewBox="0 0 500 628" aria-hidden="true">
    <g fill="none" stroke="#ffffff" stroke-width="2.5">
      <circle cx="63" cy="65" r="29"/>
      <circle cx="63" cy="65" r="23" stroke-width="1.5"/>
      <polyline points="85,86 104,99 362,99"/>

      <circle cx="30" cy="143" r="29"/>
      <circle cx="30" cy="143" r="23" stroke-width="1.5"/>
      <polyline points="58,132 72,120 362,120"/>

      <circle cx="177" cy="181" r="29"/>
      <circle cx="177" cy="181" r="23" stroke-width="1.5"/>
      <polyline points="198,202 216,222 362,222"/>

      <circle cx="45" cy="352" r="29"/>
      <circle cx="45" cy="352" r="23" stroke-width="1.5"/>
      <polyline points="66,373 88,389 362,389"/>
    </g>
  </svg>

  <p class="price-label price-forehead">Forehead $58</p>
  <p class="price-label price-frown">Frown lines $116</p>
  <p class="price-label price-crows">Crows feet $116</p>
  <p class="price-label price-lips">Lip fillers $380</p>

  <div class="title-band"></div>
  <h1 class="business-name">
    <span class="line-one">Brellmoor</span>
    <span class="line-two">Cosmetic Doctor</span>
  </h1>

  <p class="call-line">Call Us Today: 0400 559 271</p>
</main>
</body>
</html>
```